Online Course Page

We are building a video based online course page. This project is for only the actual page that the student will watch the videos at. They will watch one vide at a time. Once one video lesson is completed then they can move to the next video lesson. The page will need to show the video player. (Main feature.) The list of lessons in the course. Instructor information. Profile picture and bio of the instructor. A Live chat button that will initiate a chat in real-time with the instructor.

The winning designer will also be asked to to design the dashboard area and other aspects of the user interface as an additional project.

Target Market(s)

Adults

Number of Pages Required

1 page

Colors
9bcb3c

Requirements
Must have
• Our logo is attached. Green and grey are our colors. Should feel modern, clean and be simple to navigate. The site will be responsive so the layout should work well on mobile devices.

```html
<!DOCTYPE html>
<html lang="en">
<head>
<meta charset="utf-8">
<title>Learning Harbor – Course Page</title>
<link href="https://fonts.googleapis.com/css2?family=Acme&family=Open+Sans:wght@400;600;700&display=swap" rel="stylesheet">
<style>
  :root {
    --green: #9bcb3c;
    --green-band: #8cc231;
    --green-soft: #dcecc4;
    --ink: #1e1e1e;
    --grey: #6f6f6f;
    --grey-light: #9a9a9a;
    --line: #e3e3e3;
    --footer: #1c1c1c;
    --white: #ffffff;
  }
  * { box-sizing: border-box; margin: 0; padding: 0; }
  html, body { width: 1200px; height: 2761px; overflow: hidden; }
  body { position: relative; background: var(--white); font-family: "Open Sans", Arial, sans-serif; color: var(--ink); }
  .abs { position: absolute; }

  /* Header */
  .topline { left: 0; top: 0; width: 1200px; height: 4px; background: var(--green); }
  .site-header { left: 0; top: 4px; width: 1200px; height: 114px; background: var(--white); }
  .brand { display: flex; align-items: center; gap: 10px; font-family: "Acme", sans-serif; font-size: 30px; color: var(--ink); }
  .brand-dot { width: 30px; height: 30px; border-radius: 50%; background: var(--green); }
  .site-header .brand { position: absolute; left: 100px; top: 38px; }
  .main-nav { position: absolute; left: 400px; top: 50px; display: flex; gap: 46px; font-size: 16px; font-weight: 600; color: #222; }
  .btn { display: inline-flex; align-items: center; justify-content: center; gap: 8px; border-radius: 24px; font-weight: 700; font-size: 14px; text-transform: uppercase; letter-spacing: .3px; }
  .btn-login { position: absolute; left: 874px; top: 42px; width: 106px; height: 38px; background: var(--green); color: var(--white); }
  .btn-signup { position: absolute; left: 988px; top: 42px; width: 114px; height: 38px; border: 2px solid var(--green); color: var(--green); }

  /* Hero */
  .hero-photo { left: 0; top: 118px; width: 1200px; height: 510px; background: linear-gradient(120deg, #b08a68 0%, #8d7662 35%, #6d6a69 65%, #3f3f43 100%); }
  .hero-shade { left: 0; top: 118px; width: 1200px; height: 510px; background: rgba(40,40,40,.35); }
  .hero-title { left: 0; top: 318px; width: 1200px; text-align: center; font-family: "Acme", sans-serif; font-size: 62px; color: var(--white); }
  .hero-sub { left: 0; top: 410px; width: 1200px; text-align: center; font-size: 16px; font-weight: 600; color: var(--white); }
  .live-chat { left: 1160px; top: 314px; width: 40px; height: 118px; background: var(--green); color: var(--white); display: flex; align-items: center; justify-content: center; }
  .live-chat span { transform: rotate(-90deg); white-space: nowrap; font-size: 13px; font-weight: 700; letter-spacing: .5px; }

  .player { left: 214px; top: 486px; width: 774px; height: 448px; background: var(--white); padding: 4px; box-shadow: 0 2px 8px rgba(0,0,0,.12); }
  .player-screen { width: 100%; height: 100%; background: linear-gradient(110deg, #c9d7df 0%, #8da0ab 40%, #4a6275 75%, #2f4a60 100%); position: relative; }
  .play { position: absolute; width: 64px; height: 64px; border: 3px solid var(--white); border-radius: 50%; display: flex; align-items: center; justify-content: center; }

  /* Courses */
  .blob { border-radius: 50%; background: radial-gradient(circle, var(--green-soft) 0%, rgba(220,236,196,0) 70%); }
  .section-title { font-family: "Acme", sans-serif; font-size: 46px; color: var(--ink); }
  .section-title em { font-style: normal; color: var(--green); }
  .courses-title { left: 0; top: 998px; width: 1200px; text-align: center; }
  .course-card { top: 1088px; width: 320px; height: 264px; background: var(--white); padding: 4px; box-shadow: 0 1px 6px rgba(0,0,0,.12); }
  .course-card .thumb { width: 100%; height: 100%; position: relative; }
  .course-card .play { left: 128px; top: 100px; width: 56px; height: 56px; }
  .btn-outline { border: 2px solid var(--green); color: var(--green); background: var(--white); }
  .view-all { left: 498px; top: 1400px; width: 204px; height: 48px; }

  /* Green band */
  .band { left: 0; top: 1535px; width: 1200px; height: 407px; background: var(--green-band); }
  .band-title { left: 100px; top: 1592px; width: 620px; font-family: "Acme", sans-serif; font-size: 33px; line-height: 44px; color: var(--white); }
  .band-text { left: 100px; top: 1690px; width: 820px; font-size: 13.5px; line-height: 29px; color: var(--white); }
  .band-btn { left: 100px; top: 1829px; width: 154px; height: 46px; border: 2px solid var(--white); color: var(--white); }

  /* About */
  .about-title { left: 108px; top: 2030px; }
  .about-text { left: 108px; top: 2098px; width: 582px; font-size: 12.8px; line-height: 30px; color: var(--grey); }
  .about-btn { left: 108px; top: 2328px; width: 140px; height: 44px; background: var(--green); color: var(--white); }
  .portrait { left: 743px; top: 2010px; width: 350px; height: 350px; border-radius: 50%; border: 4px solid var(--white); box-shadow: 0 0 0 2px var(--line); background: radial-gradient(circle at 30% 35%, #7a5630 0%, #3a2c22 45%, #15181f 100%); }

  /* Footer */
  .footer-wedge { left: 0; top: 2455px; width: 1200px; height: 42px; }
  .site-footer { left: 0; top: 2496px; width: 1200px; height: 265px; background: var(--footer); color: var(--white); }
  .site-footer .brand { position: absolute; left: 100px; top: 84px; color: var(--white); font-size: 32px; }
  .divider-v { position: absolute; top: 82px; width: 1px; height: 70px; background: #3a3a3a; }
  .contact { position: absolute; top: 92px; display: flex; align-items: center; gap: 14px; font-size: 13px; line-height: 24px; font-weight: 600; }
  .ring { width: 40px; height: 40px; border: 2px solid var(--white); border-radius: 50%; display: flex; align-items: center; justify-content: center; }
  .socials { position: absolute; left: 904px; top: 92px; display: flex; gap: 10px; }
  .socials .ring { width: 42px; height: 42px; }
  .divider-h { position: absolute; left: 100px; top: 188px; width: 1000px; height: 1px; background: #2e2e2e; }
  .copyright { position: absolute; left: 0; top: 218px; width: 1200px; text-align: center; font-size: 13px; }
</style>
</head>
<body>
  <div class="abs topline"></div>
  <header class="abs site-header">
    <div class="brand"><span class="brand-dot"></span>Learning Harbor</div>
    <nav class="main-nav"><span>Home</span><span>About</span><span>Courses</span><span>News</span><span>Contact</span></nav>
    <span class="btn btn-login">
      <svg width="12" height="14" viewBox="0 0 12 14"><rect x="1" y="6" width="10" height="8" rx="1" fill="#fff"/><path d="M3 6V4a3 3 0 0 1 6 0v2" stroke="#fff" stroke-width="2" fill="none"/></svg>Log in</span>
    <span class="btn btn-signup">
      <svg width="12" height="13" viewBox="0 0 12 13"><circle cx="6" cy="3.5" r="3" fill="#9bcb3c"/><path d="M0 13a6 5 0 0 1 12 0z" fill="#9bcb3c"/></svg>Sign up</span>
  </header>

  <section aria-label="Lesson player">
    <div class="abs hero-photo" role="img" aria-label="Hands typing on a laptop keyboard"></div>
    <div class="abs hero-shade"></div>
    <h1 class="abs hero-title">Learning Harbor</h1>
    <p class="abs hero-sub">Sed utrspiciatis uomnis iste natus erroroluptatem accusium doloremque laudantium</p>
    <div class="abs player">
      <div class="player-screen" role="img" aria-label="Video lesson: learners working at computer monitors in a classroom">
        <span class="play" style="left:351px;top:188px"><svg width="20" height="24" viewBox="0 0 20 24"><path d="M3 2l15 10L3 22z" fill="none" stroke="#fff" stroke-width="2.5" stroke-linejoin="round"/></svg></span>
      </div>
    </div>
  </section>
  <a class="abs live-chat"><span>● LIVE CHAT</span></a>

  <section aria-label="Our Courses">
    <div class="abs blob" role="img" aria-label="Soft green circle decoration" style="left:-60px;top:1030px;width:340px;height:420px"></div>
    <h2 class="abs section-title courses-title">Our <em>Courses</em></h2>
    <article class="abs course-card" style="left:100px"><div class="thumb" role="img" aria-label="Lesson 1: hands on a laptop at a desk" style="background:linear-gradient(135deg,#f2d9a8,#a9a9a6 55%,#5b5f66)">
      <span class="play"><svg width="18" height="22" viewBox="0 0 20 24"><path d="M3 2l15 10L3 22z" fill="none" stroke="#fff" stroke-width="2.5" stroke-linejoin="round"/></svg></span></div></article>
    <article class="abs course-card" style="left:440px"><div class="thumb" role="img" aria-label="Lesson 2: instructor helping a learner at a computer" style="background:linear-gradient(135deg,#d7e7a8,#8fae6a 50%,#3b4a3a)">
      <span class="play"><svg width="18" height="22" viewBox="0 0 20 24"><path d="M3 2l15 10L3 22z" fill="none" stroke="#fff" stroke-width="2.5" stroke-linejoin="round"/></svg></span></div></article>
    <article class="abs course-card" style="left:782px"><div class="thumb" role="img" aria-label="Lesson 3: online learning on a laptop" style="background:linear-gradient(135deg,#2a4f86,#6f7a8c 50%,#b8aea3)">
      <span class="play"><svg width="18" height="22" viewBox="0 0 20 24"><path d="M3 2l15 10L3 22z" fill="none" stroke="#fff" stroke-width="2.5" stroke-linejoin="round"/></svg></span></div></article>
    <span class="abs btn btn-outline view-all">View all courses
      <svg width="14" height="14" viewBox="0 0 14 14"><circle cx="7" cy="7" r="7" fill="#9bcb3c"/><path d="M5.5 4l3 3-3 3" stroke="#fff" stroke-width="1.8" fill="none"/></svg></span>
  </section>

  <section aria-label="Course overview">
    <div class="abs band"></div>
    <h2 class="abs band-title">Sed ut perspiciatis unde omnis iste natus err voluptatem accusantium</h2>
    <p class="abs band-text">At vero eos et accusamus et iusto odio dignissimos ducimus qui blanditiis praesentium voluptatum deleniti atque corrupti quos dolores et quas molestias excepturi sint occaecati cupiditate non provident, similique sunt in culpa qui officia deserunt mollitia animi, id est laborum et dolorum fuga.Nam libero tempore, cum soluta nobis est eligendi optio cumque nihil impedit quo minus id quod maxime placeat facere possimus, omnis voluptas assumenda est, omnis dolor repellendus.</p>
    <span class="abs btn band-btn">Read more
      <svg width="14" height="14" viewBox="0 0 14 14"><circle cx="7" cy="7" r="7" fill="#fff"/><path d="M5.5 4l3 3-3 3" stroke="#8cc231" stroke-width="1.8" fill="none"/></svg></span>
  </section>

  <section aria-label="About the instructor">
    <div class="abs blob" role="img" aria-label="Soft green circle decoration" style="left:960px;top:2020px;width:300px;height:380px"></div>
    <h2 class="abs section-title about-title">About <em>Me</em></h2>
    <p class="abs about-text">Sed ut perspiciatis unde omnis iste natus error sit voluptatem accusantium doloremque laudantium, totam rem aperiam, eaque ipsa quae ab illo inventore veritatis et quasi architecto beatae vitae dicta sunt explicaboemo enim ipsam voluptatem quia volut aut reiciendis voluptatibus maiores alias consequatur uptas sit aspernatur aut odit autquia consequuntur..<br>Quis autem vel eum iure reprehenderit qui in ea voluptate velit esse quam nihil molestiae conillum qui dolorem eum fugiat quo voluptas nulla paremporibus autem quiut aut reiciendis voluptatibus maiores alias cdam et aut officiis debitis aut rerum necessitatibus..</p>
    <span class="abs btn about-btn">Read more
      <svg width="14" height="14" viewBox="0 0 14 14"><circle cx="7" cy="7" r="7" fill="#fff"/><path d="M5.5 4l3 3-3 3" stroke="#9bcb3c" stroke-width="1.8" fill="none"/></svg></span>
    <div class="abs portrait" role="img" aria-label="Instructor profile photo: man working on a laptop in front of warm city lights"></div>
  </section>

  <svg class="abs footer-wedge" viewBox="0 0 1200 42" preserveAspectRatio="none"><polygon points="0,42 1200,0 1200,42" fill="#9bcb3c"/></svg>
  <footer class="abs site-footer">
    <div class="brand"><span class="brand-dot"></span>Learning Harbor</div>
    <span class="divider-v" style="left:378px"></span>
    <div class="contact" style="left:418px">
      <span class="ring"><svg width="18" height="18" viewBox="0 0 24 24"><path d="M6.6 10.8a15 15 0 0 0 6.6 6.6l2.2-2.2a1 1 0 0 1 1-.25 11.4 11.4 0 0 0 3.6.6 1 1 0 0 1 1 1V20a1 1 0 0 1-1 1A17 17 0 0 1 3 4a1 1 0 0 1 1-1h3.5a1 1 0 0 1 1 1c0 1.25.2 2.45.6 3.6a1 1 0 0 1-.25 1z" fill="#fff"/></svg></span>
      <div>Call Us<br>1 800 555 0147</div>
    </div>
    <div class="contact" style="left:604px">
      <span class="ring"><svg width="18" height="14" viewBox="0 0 18 14"><rect width="18" height="14" rx="2" fill="#fff"/><path d="M1 2l8 6 8-6" stroke="#1c1c1c" stroke-width="1.6" fill="none"/></svg></span>
      <div>For Email Support<br>hello@learningharbor.com</div>
    </div>
    <span class="divider-v" style="left:866px"></span>
    <div class="socials" aria-label="Social links">
      <span class="ring"></span><span class="ring"></span><span class="ring"></span><span class="ring"></span>
    </div>
    <span class="divider-h"></span>
    <p class="copyright">Copyright © 2018 Learning Harbor. - All rights reserved &nbsp;|&nbsp; Privacy policy</p>
  </footer>
</body>
</html>
```